Platelet Rich Plasma (PRP) Flyer

Hi,

Looking to spruce up our Platelet Rich Plasma Flyer (see power point attachment). I also included previous flyers as examples on the design style we are looking for.

Quorum is our official font of our logo.
Attached is our logo in EPS format.
Please use the current photos in the power point. If you include photos, please make sure the stock image is free.

Files must be under 5MB. JPEG, PNG, PDF, .ai

Thank you,
Dorian

Target Market(s)

Patients

Industry/Entity Type

Healthcare

Font styles to use
Other font styles liked:
• Quorum

Requirements
Must have
• Emphasis on Platelet Rich Plasma Therapy when they pick up the flyer. The price of $199. FSA/HSA Eligible. The different treatment areas. The three addresses. Best of the best logo can be very small, not as important.
Nice to have
• One or two pictures. Less is more
Should not have
• Long paragraphs, multiple sentences.

```html
<!DOCTYPE html>
<html lang="en">
<head>
<meta charset="utf-8">
<title>Platelet Rich Plasma Therapy – Riverbend Foot &amp; Ankle</title>
<link rel="stylesheet" href="https://fonts.googleapis.com/css2?family=Montserrat:wght@400;700;800&family=Open+Sans:wght@400;600;700&family=Lato:wght@400;700&display=swap">
<style>
  :root {
    --bg: #333333;
    --band: #2a2a2a;
    --teal: #55c2a6;
    --orange: #f4804c;
    --white: #ffffff;
    --light: #e9e9e9;
    --ink: #262626;
  }
  * { margin: 0; padding: 0; box-sizing: border-box; }
  html, body { width: 927px; height: 1200px; overflow: hidden; background: var(--bg); }
  .flyer { position: relative; width: 927px; height: 1200px; background: var(--bg); color: var(--white); font-family: "Lato", sans-serif; overflow: hidden; }

  .brand { position: absolute; left: 44px; top: 48px; display: flex; align-items: center; gap: 14px; }
  .brand-mark { width: 40px; height: 40px; border-radius: 50%; background: var(--teal); }
  .brand-name { font-family: "Open Sans", sans-serif; font-weight: 700; font-size: 30px; line-height: 1.05; color: var(--orange); }
  .brand-name small { display: block; font-size: 15px; letter-spacing: 1px; }

  .contact { position: absolute; left: 582px; top: 53px; display: flex; align-items: center; gap: 23px; }
  .contact-icon { width: 52px; height: 52px; border-radius: 50%; background: #5a3d31; display: flex; align-items: center; justify-content: center; }
  .contact-icon span { width: 38px; height: 38px; border-radius: 50%; background: var(--orange); display: flex; align-items: center; justify-content: center; }
  .contact-label { font-family: "Open Sans", sans-serif; font-size: 15px; }
  .contact-phone { font-family: "Open Sans", sans-serif; font-weight: 700; font-size: 31px; line-height: 1.1; }

  .services { position: absolute; left: 0; top: 160px; width: 927px; height: 40px; background: var(--band); display: flex; align-items: center; justify-content: center; gap: 30px; font-family: "Open Sans", sans-serif; font-size: 19px; padding-right: 20px; }
  .services i { width: 7px; height: 7px; border-radius: 50%; background: var(--teal); display: block; }

  .visuals { position: absolute; left: 0; top: 200px; }

  .headline { position: absolute; left: 38px; top: 262px; font-family: "Montserrat", sans-serif; font-weight: 800; font-size: 57px; line-height: 68px; color: var(--teal); letter-spacing: -0.5px; }
  .headline .hot { color: var(--orange); }

  .intro { position: absolute; left: 44px; top: 486px; width: 410px; font-size: 19px; line-height: 33.4px; }
  .intro p + p { margin-top: 14px; }

  .treating { position: absolute; left: 634px; top: 483px; width: 293px; height: 298px; background: var(--teal); border-radius: 40px 0 0 40px; padding: 32px 0 0 42px; }
  .treating h2 { font-family: "Montserrat", sans-serif; font-weight: 800; font-size: 29px; margin-bottom: 22px; }
  .treating ul { list-style: none; font-family: "Montserrat", sans-serif; font-weight: 400; font-size: 17.5px; line-height: 33.5px; }
  .treating li { position: relative; padding-left: 27px; }
  .treating li svg { position: absolute; left: 0; top: 9px; }

  .price { position: absolute; left: 649px; top: 722px; width: 278px; height: 146px; background: var(--orange); border-radius: 38px 0 0 38px; padding: 26px 0 0 33px; font-family: "Montserrat", sans-serif; font-size: 19px; line-height: 28px; box-shadow: -4px 6px 14px rgba(0,0,0,0.25); }
  .price strong { font-weight: 800; font-size: 19.5px; }
  .price-note { display: block; margin-top: 4px; font-weight: 700; font-size: 15px; letter-spacing: 0.5px; }

  .availability { position: absolute; left: 0; top: 886px; width: 927px; text-align: center; font-family: "Open Sans", sans-serif; font-weight: 600; font-size: 24px; line-height: 38px; }

  .office { position: absolute; top: 1008px; width: 267px; height: 145px; border-radius: 8px; text-align: center; font-family: "Open Sans", sans-serif; font-size: 17.5px; line-height: 27px; padding-top: 46px; }
  .office h3 { font-size: 17.5px; font-weight: 700; }
  .office-pin { position: absolute; left: 50%; top: -22px; margin-left: -22px; width: 44px; height: 44px; border-radius: 50%; background: var(--bg); display: flex; align-items: center; justify-content: center; padding-top: 14px; }
  .office--north { left: 44px; background: var(--orange); color: #fff7e3; }
  .office--lake { left: 330px; background: var(--teal); }
  .office--hill { left: 616px; background: var(--light); color: var(--ink); }

  .code { position: absolute; right: 12px; bottom: 6px; font-family: Arial, sans-serif; font-size: 14px; }
</style>
</head>
<body>
<main class="flyer">
  <header>
    <div class="brand">
      <span class="brand-mark"></span>
      <div class="brand-name">Riverbend Foot &amp; Ankle<small>STRIDEWELLFEET.COM</small></div>
    </div>
    <div class="contact">
      <div class="contact-icon"><span>
        <svg width="18" height="18" viewBox="0 0 24 24"><path fill="#fff" d="M6.6 10.8a15.1 15.1 0 0 0 6.6 6.6l2.2-2.2c.3-.3.7-.4 1-.2 1.1.4 2.3.6 3.6.6.6 0 1 .4 1 1V20c0 .6-.4 1-1 1A17 17 0 0 1 3 4c0-.6.4-1 1-1h3.5c.6 0 1 .4 1 1 0 1.3.2 2.5.6 3.6.1.3 0 .7-.2 1z"/></svg>
      </span></div>
      <div>
        <div class="contact-label">Get in touch with us</div>
        <div class="contact-phone">(877) 555 - 0142</div>
      </div>
    </div>
  </header>

  <nav class="services">
    <span>Podiatry</span><i></i><span>Foot &amp; Ankle Surgery</span><i></i><span>Sports Medicine</span><i></i><span>Wound Care</span>
  </nav>

  <svg class="visuals" width="927" height="600" viewBox="0 200 927 600">
    <defs>
      <clipPath id="below-nav"><rect x="0" y="200" width="927" height="600"/></clipPath>
      <linearGradient id="lab-tone" x1="0" y1="0" x2="1" y2="1">
        <stop offset="0" stop-color="#efe6dc"/><stop offset="0.55" stop-color="#d8d8de"/><stop offset="1" stop-color="#9aa3b8"/>
      </linearGradient>
      <radialGradient id="leg-tone" cx="0.55" cy="0.45" r="0.6">
        <stop offset="0" stop-color="#c0473a"/><stop offset="0.45" stop-color="#8a5a48"/><stop offset="1" stop-color="#2b4a63"/>
      </radialGradient>
    </defs>
    <g clip-path="url(#below-nav)">
      <circle cx="730" cy="405" r="236" fill="url(#lab-tone)" role="img" aria-label="Photo of gloved hands placing blood sample tubes into a centrifuge"/>
      <circle cx="640" cy="618" r="168" fill="url(#leg-tone)" role="img" aria-label="Photo of a person holding a sore, reddened ankle"/>
    </g>
  </svg>

  <h1 class="headline">PLATELET<br>RICH <span class="hot">PLASMA</span><br><span class="hot">THERAPY</span></h1>

  <section class="intro">
    <p>PRP uses the healing proteins found in your own blood.</p>
    <p>Injected into damaged tissue, it speeds repair and new cell growth.</p>
    <p>A consultation is required to make sure you qualify.</p>
  </section>

  <section class="treating">
    <h2>TREATING</h2>
    <ul>
      <li><svg width="16" height="16" viewBox="0 0 16 16"><circle cx="8" cy="8" r="8" fill="#f4804c"/><path d="M4.5 8.2l2.3 2.3 4.7-4.7" stroke="#fff" stroke-width="2" fill="none"/></svg>Plantar Fasciitis</li>
      <li><svg width="16" height="16" viewBox="0 0 16 16"><circle cx="8" cy="8" r="8" fill="#f4804c"/><path d="M4.5 8.2l2.3 2.3 4.7-4.7" stroke="#fff" stroke-width="2" fill="none"/></svg>Achilles Tendonitis</li>
      <li><svg width="16" height="16" viewBox="0 0 16 16"><circle cx="8" cy="8" r="8" fill="#f4804c"/><path d="M4.5 8.2l2.3 2.3 4.7-4.7" stroke="#fff" stroke-width="2" fill="none"/></svg>Tendon &amp; Ligament Injuries</li>
    </ul>
  </section>

  <aside class="price">Self pay price:<br><strong>$199 per treatment</strong><span class="price-note">FSA/HSA Eligible</span></aside>

  <p class="availability">Same Day | Emergency | Saturday Appointments<br>Our Doctors are on call at the RMC ER 24/7</p>

  <section class="office office--north">
    <span class="office-pin"><svg width="14" height="18" viewBox="0 0 14 18"><path d="M7 0a7 7 0 0 0-7 7c0 5 7 11 7 11s7-6 7-11a7 7 0 0 0-7-7zm0 9.5A2.5 2.5 0 1 1 7 4.5a2.5 2.5 0 0 1 0 5z" fill="#fff"/></svg></span>
    <h3>Northside Office&nbsp;&nbsp;58</h3>
    Carroll Ridge Dr. Ste. 120<br>Millbrook, MD 21090
  </section>
  <section class="office office--lake">
    <span class="office-pin"><svg width="14" height="18" viewBox="0 0 14 18"><path d="M7 0a7 7 0 0 0-7 7c0 5 7 11 7 11s7-6 7-11a7 7 0 0 0-7-7zm0 9.5A2.5 2.5 0 1 1 7 4.5a2.5 2.5 0 0 1 0 5z" fill="#fff"/></svg></span>
    <h3>Lakeview Office</h3>
    2715 Harlow Blvd.<br>Ste. 305 Lakeview, MD 21095
  </section>
  <section class="office office--hill">
    <span class="office-pin"><svg width="14" height="18" viewBox="0 0 14 18"><path d="M7 0a7 7 0 0 0-7 7c0 5 7 11 7 11s7-6 7-11a7 7 0 0 0-7-7zm0 9.5A2.5 2.5 0 1 1 7 4.5a2.5 2.5 0 0 1 0 5z" fill="#fff"/></svg></span>
    <h3>Hillcrest Office</h3>
    480 Wellness Way<br>Hillcrest, WV 25490
  </section>

  <span class="code">C50</span>
</main>
</body>
</html>
```